GUARANTEED WordPress design needed for a sassy, confident charisma coach!

We need a website design for Marla Penrick's brand new, responsive, Wordpress website.
Marla is a trainer / coach who teaches people how to be more charismatic and runs events, publishes video courses and has an ongoing video blog. Her old website is here: www.marlapenrick.co.uk ... but it's now time to have a much better site!
We have a strong idea about the technical components of the website, but we need a designer's eye to create a great style for the site (and provide layered PSD files which our developers will then convert to HTML and CSS).
Marla's brand is sassy, brave, warm and confident. The videos on her existing site give quite a good feel for her personality. We need a clean, stylish and compelling page that isn't too corporate and captures her personality. Every element needs to feel coherent, from fonts and headings to colours and spacing.
The following sites are not exactly what Marla wants (and certainly aren't right in terms of colours) but they give you an idea of the kind of people she is competing against and the area she is operating in:
http://www.tessa-broughley.example/
http://rowanfelsby.example/
Ideally, you will have done something similar and be able to key in on exactly the kind of thing we want: we're not looking to reinvent the wheel. Hopefully you won't mind tweaking a few things if you are close to what we need.
More detail is provided in the word document attached. But in a nutshell we need: a banner, footer, sign-up strap, menu bar, signature and 4 different basic page types. We want bursts of bright colours, contrasted with black and white if possible - sorry we can't be more specific than that...
The word doc also contains some amateur mock-ups as well (the images are also just mockups at this stage) - but although these give a general sense of the structure what we are looking for, we are clearly not designers...so please help! We need a designer's touch!
Kind regards,
Corin
PS The layered PSD versions of the mockup files are available on Cloudvantre: https://files.cloudvantre.example/sh/k72pqa4w1zbtmrd/QXvenlr8Ty3PwMiU6Hs2kYfDb?dl=0
Target Market(s)
Entrepreneurs who need to sell themselves.
Number of Pages Required
4 page

```html
<!DOCTYPE html>
<html lang="en">
<head>
<meta charset="utf-8">
<title>Marla Penrick – Charisma Coach</title>
<link rel="stylesheet" href="https://fonts.googleapis.com/css2?family=Raleway:wght@400;600;700;800&family=Open+Sans:wght@400;600;700&display=swap">
<style>
  :root{
    --purple:#7b2d8e;
    --purple-dark:#5e1f6e;
    --lime:#a6c31c;
    --lime-dark:#8fab10;
    --grey-bg:#e9e9e9;
    --card:#ffffff;
    --text:#555555;
    --text-light:#8a8a8a;
    --ink:#1b1b1b;
    --cyan:#2bb8e0;
    --orange:#f2a31b;
    --photo-warm:#c9605a;
    --photo-warm-soft:#d98a84;
    --photo-neutral:#b9b9b9;
    --photo-neutral-soft:#d6d6d6;
  }
  *{box-sizing:border-box;margin:0;padding:0}
  html,body{width:1200px;height:3308px;overflow:hidden}
  body{position:relative;background:var(--grey-bg);font-family:"Open Sans",Arial,sans-serif;color:var(--text)}
  .abs{position:absolute}

  /* header */
  .site-header{left:0;top:0;width:1200px;height:60px;background:#fff;box-shadow:0 1px 4px rgba(0,0,0,.08);z-index:3}
  .brand{left:30px;top:12px;font-family:"Raleway",sans-serif;font-weight:700;font-size:28px;color:var(--purple)}
  .main-nav{right:30px;top:16px;display:flex;gap:6px}
  .main-nav a{font-family:"Raleway",sans-serif;font-size:12px;font-weight:700;color:#666;text-decoration:none;padding:6px 12px;letter-spacing:.5px}
  .main-nav a.current{border:1px solid #bbb;color:var(--purple)}

  /* hero */
  .hero{left:0;top:60px;width:1200px;height:460px;background:linear-gradient(180deg,#f5f5f5,#dedede)}
  .hero-title{left:80px;top:118px;font-family:"Raleway",sans-serif;font-weight:800;font-size:54px;line-height:1.05;color:var(--purple);letter-spacing:1px}
  .hero-copy{left:80px;top:246px;width:460px;font-size:14px;line-height:1.6;color:#666}
  .hero-portrait{left:800px;top:70px;width:250px;height:450px;background:linear-gradient(180deg,var(--photo-warm-soft),var(--photo-warm))}

  /* opt-in strap */
  .optin{left:0;top:490px;width:1200px;height:160px}
  .optin-laptop{left:80px;top:440px;width:260px;height:200px;border-radius:10px;background:linear-gradient(180deg,#3b3b3b,#2a2a2a);z-index:2}
  .optin-text{left:400px;top:536px;width:560px;font-size:18px;line-height:1.4;color:#fff;font-weight:600}
  .optin-form{left:400px;top:592px;display:flex;gap:10px}
  .field{width:160px;height:30px;background:#fff;border:none;font-size:12px;color:#999;padding:7px 10px;font-family:inherit}
  .btn{height:30px;padding:0 18px;background:var(--purple);color:#fff;font-size:12px;font-weight:700;display:flex;align-items:center;font-family:inherit}
  .optin-note{left:400px;top:628px;font-size:10px;color:#f2f7d8}

  /* posts */
  .post{left:80px;width:780px;height:500px;background:var(--card);padding:20px}
  .post-image{position:relative;width:740px;height:330px;overflow:hidden}
  .post-image .tile-text{position:absolute;left:30px;top:40px;font-family:"Raleway",sans-serif;font-weight:600;font-size:44px;line-height:1.15;color:#fff;text-transform:uppercase}
  .post-image .photo{position:absolute;top:0;right:0;height:330px}
  .post-title{margin-top:20px;font-family:"Raleway",sans-serif;font-weight:800;font-size:19px;color:var(--purple);text-transform:uppercase}
  .post-excerpt{margin-top:10px;font-size:13px;line-height:1.55;color:#777;width:720px}
  .post-excerpt b{color:var(--purple);font-weight:700}
  .post-meta{margin-top:12px;display:flex;gap:28px;font-size:11px;color:var(--text-light);text-transform:uppercase}
  .post-meta span::before{content:"";display:inline-block;width:9px;height:9px;border:1px solid #aaa;margin-right:6px;vertical-align:-1px}

  .pager{left:300px;top:2936px;display:flex;gap:12px}
  .pager span{width:24px;height:24px;border-radius:50%;border:2px solid #999;font-size:11px;color:#777;display:flex;align-items:center;justify-content:center}
  .pager span.on{background:#999;color:#fff}

  /* sidebar */
  .widget{left:890px;width:230px;background:var(--card);padding:16px}
  .widget h3{font-family:"Raleway",sans-serif;font-weight:800;font-size:15px;color:var(--purple);padding-bottom:10px;border-bottom:3px solid var(--purple);margin-bottom:12px}
  .says li{list-style:none;font-size:12px;line-height:1.4;color:#555;padding:8px 0;border-bottom:1px solid #eee}
  .says small{display:block;font-size:10px;color:var(--text-light);margin-top:3px}
  .tags{display:flex;flex-wrap:wrap;gap:5px}
  .tags span{background:var(--purple);color:#fff;font-size:12px;padding:3px 8px}
  .tags span.lg{font-size:18px}
  .tags span.md{font-size:15px}
  .video-thumb{width:198px;height:150px;background:linear-gradient(90deg,var(--photo-neutral-soft),var(--photo-neutral))}
  .promo{position:relative;width:198px;height:600px;background:linear-gradient(180deg,#6d2880 0%,#4a2c50 100%);padding:16px}
  .promo-head{font-family:"Raleway",sans-serif;font-weight:800;font-size:22px;line-height:1.15;color:#fff}
  .promo-live{position:absolute;left:16px;top:330px;font-family:"Raleway",sans-serif;font-weight:800;font-size:52px;color:#fff}
  .promo-places{position:absolute;left:60px;top:400px;font-size:18px;line-height:1.2;color:#fff;font-style:italic}
  .promo-btn{position:absolute;left:16px;top:470px;width:120px;background:var(--cyan);color:#fff;font-family:"Raleway",sans-serif;font-weight:800;font-size:18px;text-align:center;padding:8px 0}
  .standing{left:905px;top:2520px;width:190px;height:680px;background:linear-gradient(180deg,var(--photo-neutral-soft),var(--photo-neutral));z-index:2}

  /* signup strap */
  .signup{left:0;top:3030px;width:1200px;height:170px;background:var(--purple)}
  .signup-text{left:80px;top:3060px;width:720px;font-size:17px;line-height:1.45;color:#fff;text-align:center}
  .signup-form{left:230px;top:3130px;display:flex;gap:10px}
  .signup-form .btn{background:var(--lime);color:var(--ink)}

  /* footer */
  .site-footer{left:0;top:3200px;width:1200px;height:108px;background:var(--ink)}
  .copyright{left:80px;top:3226px;font-size:12px;color:#ccc}
  .legal{left:80px;top:3256px;display:flex;gap:22px;font-size:10px;color:#999;text-transform:uppercase}
  .social{left:940px;top:3226px;display:flex;gap:8px}
  .social span{width:30px;height:30px;background:#3f7fc4}
</style>
</head>
<body>

<header class="site-header abs">
  <div class="brand abs">Marla Penrick</div>
  <nav class="main-nav abs">
    <a class="current">HOME</a><a>EVENTS</a><a>WORK WITH ME</a><a>CORPORATE</a><a>ABOUT</a><a>CONTACT</a>
  </nav>
</header>

<section class="hero abs"></section>
<h1 class="hero-title abs">ATTRACT CONNECT<br>INFLUENCE</h1>
<p class="hero-copy abs">Charisma is a skill you can learn. I help entrepreneurs walk into any room with presence, warmth and the confidence to win the work they deserve.</p>
<div class="hero-portrait abs" role="img" aria-label="Photo of Marla smiling in a red dress"></div>

<svg class="optin abs" viewBox="0 0 1200 160" preserveAspectRatio="none" aria-hidden="true">
  <path d="M0 40 C 300 0, 700 10, 1200 30 L1200 160 L0 160 Z" fill="var(--lime)"/>
  <path d="M0 120 C 400 150, 800 150, 1200 120 L1200 160 L0 160 Z" fill="var(--lime-dark)"/>
</svg>
<div class="optin-laptop abs" role="img" aria-label="Laptop showing a training video with Marla"></div>
<p class="optin-text abs">Learn how to unlock the “superpower” of your charisma and win all the business you want with this FREE training.</p>
<div class="optin-form abs">
  <div class="field">First Name</div><div class="field">Email Address</div><div class="btn">Yes Please</div>
</div>
<p class="optin-note abs">* I promise never to share your email address.</p>

<article class="post abs" style="top:700px">
  <div class="post-image" style="background:linear-gradient(135deg,#1d1d1d,#3a3a3a)">
    <div class="photo" role="img" aria-label="Audience watching a speaker on stage" style="left:0;width:740px;background:linear-gradient(90deg,rgba(60,40,40,.2),rgba(90,60,60,.6))"></div>
    <div class="tile-text">Public<br>Speaking...</div>
  </div>
  <h2 class="post-title">Public speaking...made easy</h2>
  <p class="post-excerpt">Your voice, posture and pace decide how a room hears you long before your slides do. Here are simple ways to speak with calm, clear authority every single time. <b>Continue Reading</b></p>
  <div class="post-meta"><span>May 23 2016</span><span>0 Comments</span></div>
</article>

<article class="post abs" style="top:1244px">
  <div class="post-image" style="background:#3b3b3b">
    <div class="photo" role="img" aria-label="Photo of Marla laughing" style="width:300px;background:linear-gradient(180deg,#555,#6e6e6e)"></div>
    <div class="tile-text" style="font-size:40px">How to start<br>every day in<br>the right<br>frame of mind!</div>
  </div>
  <h2 class="post-title">How to start every day in the right frame of mind!</h2>
  <p class="post-excerpt">The first hour of your morning sets the tone for every meeting that follows. Try this short routine to wake up focused, upbeat and ready to shine. <b>Continue Reading</b></p>
  <div class="post-meta"><span>May 23 2016</span><span>0 Comments</span></div>
</article>

<article class="post abs" style="top:1788px">
  <div class="post-image" style="background:var(--cyan)">
    <div class="photo" role="img" aria-label="Marla holding a magazine" style="width:220px;background:linear-gradient(180deg,#7fd3ec,#a9e1f2)"></div>
    <div class="tile-text" style="font-size:42px">Take charge of your<br>style...<span style="font-size:34px">boost your</span><br>confidence</div>
  </div>
  <h2 class="post-title">Take charge of your style...boost your confidence</h2>
  <p class="post-excerpt">What you wear speaks before you do. Small changes to colour, fit and detail can lift how you feel and how clients see you from the very first glance. <b>Continue Reading</b></p>
  <div class="post-meta"><span>May 23 2016</span><span>0 Comments</span></div>
</article>

<article class="post abs" style="top:2332px">
  <div class="post-image" style="background:var(--orange)">
    <div class="photo" role="img" aria-label="Marla in a thoughtful pose" style="width:250px;background:linear-gradient(180deg,#e3951a,#c98418)"></div>
    <div class="tile-text" style="font-size:40px;top:30px">Unfulfilled? It's<br>time to think<br>about your<br>values...</div>
    <div class="tile-text" style="font-size:24px;top:262px">Do this exercise now!</div>
  </div>
  <h2 class="post-title">Unfulfilled? It's time to think about your values...</h2>
  <p class="post-excerpt">When work feels flat it is often a sign your values are out of step. This quick exercise helps you name what matters and plan your next bold move. <b>Continue Reading</b></p>
  <div class="post-meta"><span>May 23 2016</span><span>0 Comments</span></div>
</article>

<div class="pager abs"><span>‹</span><span class="on">1</span><span>2</span><span>3</span><span>4</span><span>›</span></div>

<aside class="widget abs" style="top:712px">
  <h3>MARLA SAYS</h3>
  <ul class="says">
    <li>Be more dog: 3 lessons we could learn from our best friends<small>May 23 2016</small></li>
    <li>Are you letting your nerves hold you back?<small>May 23 2016</small></li>
    <li>How I learned to stop worrying and start NETWORKING<small>May 23 2016</small></li>
    <li>Blind spots: seeing yourself the way others do<small>May 23 2016</small></li>
  </ul>
</aside>

<aside class="widget abs" style="top:1132px">
  <h3>TAGS</h3>
  <div class="tags">
    <span>body language</span><span class="lg">capsule wardrobe</span><span>confidence</span><span>handshake</span><span>nlp</span>
    <span>makeup</span><span>perception</span><span class="md">power pose</span><span>presentation</span>
    <span class="lg">rapport</span><span>relaxation</span><span>silence</span><span>vision board</span><span>warmth</span>
  </div>
</aside>

<aside class="widget abs" style="top:1480px">
  <h3>VIDEO</h3>
  <div class="video-thumb" role="img" aria-label="Video still of Marla talking to camera"></div>
</aside>

<aside class="widget abs" style="top:1800px">
  <h3>COMING UP!</h3>
  <div class="promo" role="img" aria-label="Event poster with Marla on stage">
    <div class="promo-head">UNLOCK<br>THE<br>SUPERPOWER<br>OF<br>CHARISMA</div>
    <div class="promo-live">LIVE</div>
    <div class="promo-places">Only 6<br>places left.</div>
    <div class="promo-btn">LEARN<br>MORE</div>
  </div>
</aside>

<section class="signup abs"></section>
<p class="signup-text abs">Hey! Don't go without signing up because you'll miss out on exclusive offers, awesome tips, and weekly motivation in my fab newsletter.</p>
<div class="signup-form abs">
  <div class="field">First Name</div><div class="field">Email Address</div><div class="btn">Yes Please</div>
</div>

<div class="standing abs" role="img" aria-label="Full-length photo of Marla in a black and white dress"></div>

<footer class="site-footer abs"></footer>
<p class="copyright abs">© 2016 Marla Penrick Ltd</p>
<div class="legal abs"><span>Privacy Policy</span><span>Cookie Policy</span><span>Terms Policy</span><span>Disclaimer</span></div>
<div class="social abs"><span></span><span></span><span></span><span></span><span></span></div>

</body>
</html>
```